ZELK LED WALL BUYERS GUIDE

We require a brcohure to send to our customers that sets out the provided text in a neat and clearly readable format, We wish to position this brochure as an information source that demonstrates us a market leader in this technology and not afraid to share what customers should be looking for in a new LED video wall. This will be used mostly in PDF format, will be multiple A4 pages and we are happy to include stock photos where required to further illustrate or show the technical nature of our business and products. Plenty of white space and easy to read is a MUST for this project. We have uploaded the text document and the logo we which to incorporate into this brochure.Brochure should include all our office address's (located at www.kemtrix.com.au)

Target Market(s)

Corporate, education, fitness, advertising, digital signage

Colors
0255a3
0455a3

Requirements
Must have
• Be easy to read, clean and tidy and be visually captivating.
• Promote our business as a knowlege based market leader
• Include the text we have already prepared
• Have our office addressed and contact numbers
• Include our corporate colours (www.kemtrix.com.au)
Nice to have
• Be easy to read
• Make potential customers "want to read it"
• We have the ZELK logo in AI and EPS format if needed

```html
<!DOCTYPE html>
<html lang="en">
<head>
<meta charset="utf-8">
<title>ZELK LED Wall Buyers Guide – Spread</title>
<link rel="stylesheet" href="https://fonts.googleapis.com/css2?family=Ubuntu:wght@400;500&family=Arimo:wght@400&display=swap">
<style>
  :root{
    --backdrop:#e9e9e9;
    --paper:#f7f7f7;
    --paper-right:#f1f1f2;
    --brand-blue:#1d6ea8;
    --spine-blue:#3a86c2;
    --accent-orange:#f2a227;
    --ink:#2a2a2a;
    --muted:#b3b3b3;
    --band:#e2e3e6;
  }
  *{box-sizing:border-box;margin:0;padding:0}
  html,body{width:1200px;height:840px;overflow:hidden;background:var(--backdrop)}
  .spread{position:absolute;left:236px;top:145px;width:730px;height:555px;display:flex;box-shadow:0 10px 30px rgba(0,0,0,.12)}
  .page{position:relative;width:365px;height:100%;font-family:"Arimo",Arial,sans-serif}
  .page--left{background:var(--paper);border-left:9px solid var(--spine-blue)}
  .page--right{background:var(--paper-right);border-right:7px solid var(--spine-blue)}
  .page__title{position:absolute;left:28px;top:103px;font-family:"Ubuntu",sans-serif;font-weight:500;font-size:12.5px;line-height:16.5px;letter-spacing:2.2px;color:var(--brand-blue);text-transform:uppercase}
  .page__title .accent{color:var(--accent-orange)}
  .lead{font-size:7px;line-height:11.5px;color:var(--ink);text-align:justify}
  .section-label{font-family:"Ubuntu",sans-serif;font-weight:500;font-size:8px;letter-spacing:1.4px;color:var(--brand-blue);text-transform:uppercase}
  .body-copy{font-size:6.8px;line-height:11.5px;color:var(--muted);text-align:justify}
  .body-copy p + p{margin-top:11px}
  .page--left .lead{position:absolute;left:28px;top:188px;width:282px}
  .page--left .section-label{position:absolute;left:28px;top:239px}
  .page--left .body-copy{position:absolute;left:28px;top:262px;width:282px}
  .page--right .lead{position:absolute;left:66px;top:104px;width:283px}
  .page--right .section-label{position:absolute;left:66px;top:155px}
  .page--right .body-copy{position:absolute;left:66px;top:178px;width:283px}
  .distance-table{position:absolute;left:58px;top:300px;width:300px;border-collapse:collapse;font-family:"Ubuntu",sans-serif;font-size:6px;letter-spacing:1.2px;color:var(--brand-blue);text-transform:uppercase}
  .distance-table th{background:var(--band);font-weight:500;text-align:left;padding:5px 0 4px 12px;vertical-align:top;line-height:8px}
  .distance-table td{padding:8px 0 0 12px}
</style>
</head>
<body>
<div class="spread">
  <section class="page page--left">
    <h1 class="page__title">What do I need to think<br>about when <span class="accent">choosing</span><br><span class="accent">a Z.E.L.K LED</span><br><span class="accent">video wall display solution?</span></h1>
    <p class="lead">There are a number of requirements that need to be considered and discussed during project planning to ensure that the right LED Video Wall solution is successfully chosen and deployed:</p>
    <h2 class="section-label">Content</h2>
    <div class="body-copy">
      <p>Understanding the required content is essential to any successful LED Video Wall installation. This is especially important when considering what shape or aspect ratio the LED display should be.<br>Interesting shapes and sizes can provide exceptional impact, but will require further investment in specialised content production to remain engaging.</p>
      <p>Standard aspect ratios might not be as creative in physical design, but allow for simpler content creation.</p>
      <p>When running multiple content sources through a video wall controller, content layouts and pre-sets should be coordinated during the Video Wall design to ensure the required content can be delivered onto the Video Wall.<br>Ideally, sample content should be created and provided for testing, or during the LED selection criteria.</p>
    </div>
  </section>
  <section class="page page--right">
    <p class="lead">There are a number of requirements that need to be considered and discussed during project planning to ensure that the right LED Video Wall solution is successfully chosen and deployed:</p>
    <h2 class="section-label">Size</h2>
    <div class="body-copy">
      <p>Industry guidelines around the overall screen size apply for LED solutions, as they do for other display technologies.</p>
      <p>If an LED display is too small, it can be difficult to read detailed information. Too big, and it can be difficult to view all of the information in one single view.</p>
      <p>Taking into account minimum viewing distances for pixel pitch as detailed below, Kemtrix Media Systems work to best practise standards when recommending the most appropriate display size for your application.</p>
    </div>
    <table class="distance-table">
      <thead>
        <tr><th>Level of detail</th><th>Example</th><th>Viewers distance<br>from display</th></tr>
      </thead>
      <tbody>
        <tr><td>Fine detail</td><td>Spreadsheet</td><td>4 x height of the display</td></tr>
        <tr><td>General</td><td>Presentation</td><td>6 x height of the display</td></tr>
        <tr><td>Video</td><td>Video</td><td>8 x height of the display</td></tr>
      </tbody>
    </table>
  </section>
</div>
</body>
</html>
```